Email Newsletter Template

We would like to email monthly newsletters and ad hoc sales focused 'call to action' email campaigns.

The template should have a fixed design with a header and footer standard with our logo and call to action details. Images and text in the body of the newsletter should be fully editable for us to modify each month.

The attached file will give you an idea of the colour and the collage image (which we use in some of our other print and online branding).

The red colour is code:
CMYK 0/100/65/25
RGB:175/10/45
PMS #187

The first email campaign we are planning on launching will involve those recipients who go through a short online accreditation winning an Telvo slate. Therefore, for that particular version of the newsletter, will would include an image of the image mini (much like the one at the link below)

http://www.brindlemart.example.au/telvo-slate-wi-fi-16gb-white.html

Target Market(s)

Business to Business. Focus on Professionals and small to medium businesses.

Industry/Entity Type

Call

Font styles to use
Other font styles liked:
• Sansation as the main font

Requirements
Must have
• Template with fixed footer - rest of document should be fully editable by us to use as a monthly e-blast with different text and images each month.

```html
<!DOCTYPE html>
<html lang="en">
<head>
<meta charset="utf-8">
<title>Quillmere Advisory – Newsletter</title>
<link rel="stylesheet" href="https://fonts.googleapis.com/css2?family=PT+Sans:wght@400;700&display=swap">
<style>
  :root {
    --brand-red: #b82c45;
    --brand-red-deep: #9e1f37;
    --accent-orange: #f6a443;
    --ink: #1f1f1f;
    --navy: #2c3a58;
    --white: #ffffff;
  }
  * { box-sizing: border-box; margin: 0; padding: 0; }
  html, body { width: 927px; height: 1200px; overflow: hidden; background: var(--white); }
  body { font-family: "PT Sans", "Helvetica Neue", Arial, sans-serif; }
  .newsletter { position: relative; width: 927px; height: 1200px; overflow: hidden; background: var(--white); }
  .backdrop { position: absolute; inset: 0; }
  .headline {
    position: absolute; left: 56px; top: 50px; white-space: nowrap;
    color: var(--white); font-size: 32px; font-weight: 400; letter-spacing: -0.1px;
  }
  .intro {
    position: absolute; left: 58px; top: 104px; white-space: nowrap;
    color: var(--accent-orange); font-size: 17px; line-height: 21px;
  }
  .cta-box {
    position: absolute; left: 59px; top: 254px; width: 473px; height: 78px;
    background: var(--white); border-radius: 11px;
    display: flex; align-items: center; padding-left: 36px;
    color: var(--brand-red); font-size: 28px; white-space: nowrap;
  }
  .prize-image {
    position: absolute; left: 129px; top: 369px; width: 333px; height: 402px;
    border-radius: 18px;
    background: linear-gradient(135deg, #f4f4f6 0%, #d9dade 45%, #5c5f78 70%, #3b3e55 100%);
  }
  .social-row { position: absolute; left: 550px; top: 906px; display: flex; gap: 9px; }
  .social-tile { width: 56px; height: 56px; border-radius: 6px; }
  .social-tile.sky { background: #5db8d9; }
  .social-tile.indigo { background: #4a5f9c; }
  .social-tile.crimson { background: #c9302c; }
  .social-tile.royal { background: #3b4ea3; }
  .social-tile.amber { background: #ef8a26; }
  .footer-quote {
    position: absolute; left: 77px; top: 1030px; white-space: nowrap;
    color: var(--ink); font-size: 19.5px; line-height: 24.5px;
  }
  .brand-mark {
    position: absolute; left: 672px; top: 1076px;
    display: flex; align-items: center; gap: 10px;
  }
  .brand-dot { width: 34px; height: 34px; border-radius: 50%; background: var(--brand-red); }
  .brand-name { color: var(--navy); font-size: 24px; font-weight: 700; white-space: nowrap; }
</style>
</head>
<body>
<main class="newsletter">
  <svg class="backdrop" width="927" height="1200" viewBox="0 0 927 1200" aria-hidden="true">
    <defs>
      <linearGradient id="footer-fade" x1="0" y1="0" x2="0" y2="1">
        <stop offset="0" stop-color="#e6e6ea"/>
        <stop offset="0.35" stop-color="#ffffff"/>
      </linearGradient>
      <linearGradient id="swoosh-line" x1="0" y1="0" x2="1" y2="0">
        <stop offset="0" stop-color="#f2a5b4"/>
        <stop offset="1" stop-color="#ffffff"/>
      </linearGradient>
    </defs>
    <rect width="927" height="1200" fill="url(#footer-fade)"/>
    <path d="M0 0 H927 V604 C720 760 380 950 0 968 Z" fill="var(--brand-red)"/>
    <path d="M0 968 C380 950 720 760 927 604" fill="none" stroke="#f3b8c3" stroke-width="3"/>
    <path d="M462 630 C640 600 820 520 927 395" fill="none" stroke="url(#swoosh-line)" stroke-width="3"/>
    <path d="M0 455 C50 500 100 560 135 610" fill="none" stroke="var(--brand-red-deep)" stroke-width="3"/>
  </svg>

  <h1 class="headline">Have you go through a short online accreditation?</h1>
  <p class="intro">Lorem ipsum dolor sit amet, per ea wisi nulla harum. Eum liber laoreet sadipscing in,<br>ne vix iriure volumus suscipiantur. Legendos periculis eu qui, ne est malorum volutpat.<br>Eam posidonium theophrastus no. Nec ad quidam repudiare disputationi,<br>ea mel wisi recteque tractatos.</p>

  <div class="cta-box">Aplay now and win an Telvo slate.</div>

  <div class="prize-image" role="img" aria-label="Product photo of a white Telvo slate tablet, front and back view"></div>

  <nav class="social-row" aria-label="Social channels">
    <span class="social-tile sky"></span>
    <span class="social-tile indigo"></span>
    <span class="social-tile crimson"></span>
    <span class="social-tile royal"></span>
    <span class="social-tile amber"></span>
  </nav>

  <p class="footer-quote">“Lorem ipsum dolor sit amet, per ea wisi nulla harum.<br>Eum liber laoreet sadipscing in, ne vix iriure volumus suscipiantur.<br>Legendos periculis eu qui, ne est malorum volutpat.<br>Eam posidonium theophrastus no. Nec ad quidam repudiare<br>disputationi, ea mel wisi recteque tractatos”.</p>

  <div class="brand-mark">
    <span class="brand-dot"></span>
    <span class="brand-name">Quillmere Advisory</span>
  </div>
</main>
</body>
</html>
```